Business Card Design Project

Velvet Harbor is a Boutique Clothing. On the business cards I would like to have this included
Website: www.velvetharbor-example.com
Email: shop@velvetharbor-example.com
Owner: Mira Sol & Tor Dell

Industry/Entity Type

Business

Contact Information for Business Card

I wanted something simple and elegant. I have attach business logo.

```html
<!DOCTYPE html>
<html lang="en">
<head>
<meta charset="utf-8">
<title>Velvet Harbor — Business Card</title>
<link rel="stylesheet" href="https://fonts.googleapis.com/css2?family=Montserrat:wght@300;400;600;700&family=Open+Sans:wght@400&display=swap">
<style>
  :root {
    --page-bg: #ffffff;
    --card-bg: #ffffff;
    --card-border: #c8c8c8;
    --accent: #f5c403;
    --ink: #2b2b2b;
    --on-accent: #ffffff;
  }
  * { box-sizing: border-box; margin: 0; padding: 0; }
  html, body {
    width: 1200px;
    height: 1200px;
    overflow: hidden;
    background: var(--page-bg);
  }
  .canvas {
    position: relative;
    width: 1200px;
    height: 1200px;
  }
  .business-card {
    position: absolute;
    left: 180px;
    top: 359px;
    width: 841px;
    height: 481px;
    background: var(--card-bg);
    border: 2px solid var(--card-border);
  }
  .brand-mark {
    position: absolute;
    left: 40px;
    top: 0;
    width: 300px;
    height: 100%;
    display: flex;
    align-items: center;
    justify-content: center;
    gap: 12px;
  }
  .brand-dot {
    width: 14px;
    height: 14px;
    border-radius: 50%;
    background: var(--ink);
  }
  .brand-name {
    font-family: "Montserrat", sans-serif;
    font-weight: 600;
    font-size: 30px;
    letter-spacing: 1px;
    color: var(--ink);
  }
  .info-panel {
    position: absolute;
    left: 365px;
    top: 17px;
    width: 451px;
    height: 442px;
    background: var(--accent);
  }
  .panel-notch {
    position: absolute;
    left: 0;
    top: 200px;
    width: 22px;
    height: 42px;
  }
  .company-name {
    position: absolute;
    left: 34px;
    top: 170px;
    font-family: "Montserrat", sans-serif;
    font-weight: 700;
    font-size: 32px;
    line-height: 1;
    color: var(--on-accent);
    white-space: nowrap;
  }
  .tagline {
    position: absolute;
    right: 34px;
    top: 206px;
    font-family: "Montserrat", sans-serif;
    font-weight: 300;
    font-size: 27px;
    line-height: 1;
    color: var(--on-accent);
    white-space: nowrap;
  }
  .contact-list {
    position: absolute;
    right: 36px;
    top: 320px;
    list-style: none;
    text-align: right;
    font-family: "Open Sans", sans-serif;
    font-size: 19px;
    line-height: 26.5px;
    color: var(--on-accent);
    white-space: nowrap;
  }
  .contact-rule {
    position: absolute;
    right: 27px;
    top: 322px;
    width: 2px;
    height: 86px;
    background: var(--on-accent);
  }
</style>
</head>
<body>
<main class="canvas">
  <article class="business-card">
    <div class="brand-mark">
      <span class="brand-dot"></span>
      <span class="brand-name">Velvet Harbor</span>
    </div>

    <section class="info-panel">
      <svg class="panel-notch" viewBox="0 0 22 42" aria-hidden="true">
        <polygon points="0,0 22,21 0,42" fill="#ffffff"/>
      </svg>
      <h1 class="company-name">Velvet Harbor</h1>
      <p class="tagline">is a Boutique Clothing</p>

      <ul class="contact-list">
        <li>Website: www.velvetharbor-example.com</li>
        <li>Email: shop@velvetharbor-example.com</li>
        <li>Owner: Mira Sol &amp; Tor Dell</li>
      </ul>
      <span class="contact-rule"></span>
    </section>
  </article>
</main>
</body>
</html>
```